!! We Need YOU !! Las Vegas !! Pool Cleaning Company looking for a Brochure Design!

We are a pool/spa/water feature cleaning company for commercial properties. We are looking for a professional looking brochure to hand to clients as we speak to them about our business. We would like something that stays away from back yard pool themes like pool toys and diving boards. Our properties are resorts, hotels, casinos, and private estates so we need something to grab their attention!

Our company name is "Premier Basin Stewards"
Our slogan is "Sparkling Results"
Phone is 702-555-0187
email is rkelvane@basinstewardsgroup.com
webpage www.premier-basin-stewardsgrp.com
(I know those are long! Sorry!)

We DO NOT need to include all of this in one brochure but here are some ideas for wording:

Swimming pools are a way of life in Las Vegas and PBS loves being a part of that culture. PBS is a company that has a team with 15 years of experience that spans across the Las Vegas Valley working on commercial properties. We understand the complexity of managing commercial pools and bring our resources and experience to provide you with a service that can not be matched.

the PBS advantage:
Since 2002 our team has had the privilege of providing services to resorts, casinos, hotels, and private estates. The tried and true business practices of our team have been tested and refined over the years. These practices have resulted in a set of standards to ensure PBS is a company of distinction. We believe our commitment to safety, integrity, affordability, and professionalism help us deliver the best possible pool cleaning services in Las Vegas.

Safety: PBS understands the specific requirements of the health department and chemical regulations. We work closely with the health department and exceed their requirements to help keep your property safe and compliant. PBS has developed a set of systems and programs that have been proven within the industry to accomplish reliance to safety. Our employees are dedicated to using the most advanced tools, training, and technology available to keep your property clean and safe.
Integrity:
You are secure with PBS. We pride ourselves on providing our customers with the right care for your property through honest and straightforward service. PBS will adhere to quality and honesty. PBS will have an active regard for our standards of conduct. It is our sincere belief that by establishing relationships through responsiveness to the customer's needs and dedication to our customers, that we will become the standard by which all other companies will measure their success.

Affordability: You can be assured that PBS will provide professional services at a reasonable rate. PBS will establish a long-term and beneficial relationship while fixing your costs for the next 1-5 years. We strive to keep our focus on commercial properties which means our focus is on your property. We offer exceptional pricing on cleaning, maintenance, and repair services.
Professionalism:
With any industry, you have a spectrum of professionalism. PBS strives to be at the top of that spectrum by encompassing all of the aforementioned qualities, plus many more. We strive to be the leader in providing quality service through education and certification. PBS employees always show respect for you and your property and are highly knowledgeable, courteous, and efficient. PBS will exceed expectations in the areas of accountability, customer support, and expertise.

We will be proactive rather than reactive to potentially problematic areas with proper advance planning.

When you work with PBS you can trust that our experience in the hospitality industry brings unlimited service, quick response, and a reputation to serve. If you have a commercial pool in the Las Vegas area, you should have our number.
If you are looking for knowledgeable and dependable pool cleaning and maintenance in Las Vegas, look no further than PBS.

Maintenance
▪ Regular Maintenance Services
▪ Weekly Pool/Spa Service
▪ One Time Clean-Ups
▪ DE Filter Cleaning
▪ Drain Pool & Refill
▪ Impellers
▪ Valves
▪ Algae Removal
▪ Back Wash
▪ Water Testing & Balancing
▪ Equipment Inspection
▪ Skimming, Brushing, & Leafing
Emergency service 24 hours per day, 7 days per week
Updates

Target Market(s)

High-end Resorts and properties.

Industry/Entity Type

It Company

Font styles to use
Serif
Sans Serif

Requirements
Must have
• Professional look and feel.
• Size/shape will depend on design concept-I do not care if it is traditional fold or something creative.
• Needs to have a front and back complete concept.
Nice to have
• I would like to see some ideas using our font and colors.
• I would like to focus on pictures with no buildings or beaches in them.
Should not have
• No pool toys, diving boards, palm trees, beach, or anything with a "backyard" pool feel.

```html
<!DOCTYPE html>
<html lang="en">
<head>
<meta charset="utf-8">
<title>Premier Basin Stewards – Brochure</title>
<link href="https://fonts.googleapis.com/css2?family=Montserrat:wght@600;700&family=Open+Sans:wght@300;400;600;700&display=swap" rel="stylesheet">
<style>
  :root{
    --sky:#5fc3ee;
    --sky-deep:#2b8fd8;
    --ocean:#1c5fb4;
    --ocean-mid:#2f7fd0;
    --slate:#6b6c6f;
    --white:#ffffff;
    --rule:rgba(255,255,255,.45);
    --brand-blue:#2c6cc0;
    --headline-blue:#7ccbf2;
  }
  *{margin:0;padding:0;box-sizing:border-box}
  html,body{width:1200px;height:815px;overflow:hidden;background:var(--white)}
  body{position:relative;font-family:"Open Sans",Arial,sans-serif;color:var(--white)}

  .brochure{position:absolute;left:122px;top:78px;width:953px;height:658px;overflow:hidden;
    background:var(--sky);border-left:1px solid #8a8a8a;border-bottom:1px solid #8a8a8a}
  .brochure__art{position:absolute;inset:0}

  .services{position:absolute;left:37px;top:64px;width:300px}
  .services__title{font-family:"Montserrat",Arial,sans-serif;font-weight:600;font-size:22px;letter-spacing:.3px}
  .services__rule{position:absolute;left:208px;top:86px;width:363px;height:1px;background:var(--rule)}
  .services__list{list-style:none;margin-top:13px;font-weight:300;font-size:12.6px;line-height:17.6px}
  .services__note{margin-top:17px;font-weight:300;font-size:12.6px;line-height:17.6px;width:250px}

  .contact{position:absolute;left:318px;top:180px;width:300px;text-align:center}
  .logo{display:flex;align-items:center;gap:8px}
  .logo__mark{width:26px;height:26px;border-radius:50%;border:3px solid currentColor;flex:none}
  .logo__name{font-family:"Montserrat",Arial,sans-serif;font-weight:700;line-height:1}
  .contact .logo{justify-content:center;margin-left:-20px}
  .contact .logo__name{font-size:42px}
  .contact__tagline{margin-top:68px;font-size:10.5px;font-weight:600}
  .contact__icon{display:block;margin:8px auto 0}
  .contact__phone{margin-top:2px;font-size:34px;font-weight:600;letter-spacing:.2px;line-height:1.1}
  .contact__line{font-size:10.5px;line-height:15px}
  .contact__phone + .contact__line{margin-top:14px}

  .cover .logo{position:absolute;right:22px;top:70px;color:var(--brand-blue)}
  .cover .logo__name{font-size:54px}
  .cover__headline{position:absolute;right:16px;top:505px;text-align:right;color:var(--headline-blue);
    font-family:"Open Sans",Arial,sans-serif;font-weight:400;font-size:25px;line-height:37px}
  .cover__slogan{position:absolute;right:16px;top:575px;font-weight:700;font-size:14.5px}
  .cover__web{position:absolute;right:14px;top:628px;font-size:8.5px}
</style>
</head>
<body>
<div class="brochure">
  <svg class="brochure__art" width="953" height="658" viewBox="0 0 953 658">
    <defs>
      <linearGradient id="middleFill" x1="0" x2="1">
        <stop offset="0" stop-color="#5cc0ee"/><stop offset="1" stop-color="#2a8bd5"/>
      </linearGradient>
      <linearGradient id="spaPhoto" x1="0" y1="0" x2="1" y2="1">
        <stop offset="0" stop-color="#3b4650"/><stop offset=".5" stop-color="#8a9a6a"/><stop offset="1" stop-color="#4c6a3a"/>
      </linearGradient>
      <linearGradient id="poolPhoto" x1="0" y1="0" x2="0" y2="1">
        <stop offset="0" stop-color="#ffffff"/><stop offset=".12" stop-color="#c9b89a"/>
        <stop offset=".4" stop-color="#6aa6c8"/><stop offset="1" stop-color="#1f78c0"/>
      </linearGradient>
      <clipPath id="coverClip"><path d="M665,0 Q592,330 690,658 L953,658 L953,0 Z"/></clipPath>
      <clipPath id="spaClip"><circle cx="143" cy="522" r="140"/></clipPath>
    </defs>
    <rect x="318" y="0" width="400" height="658" fill="url(#middleFill)"/>
    <line x1="318" y1="0" x2="318" y2="658" stroke="rgba(255,255,255,.25)"/>
    <path d="M622,0 Q552,330 652,658 L700,658 Q608,330 680,0 Z" fill="var(--ocean-mid)"/>
    <path d="M645,0 Q575,330 672,658 L700,658 Q600,330 665,0 Z" fill="var(--ocean)"/>
    <g clip-path="url(#coverClip)">
      <rect x="560" y="0" width="400" height="658" fill="var(--white)"/>
      <rect x="560" y="130" width="400" height="528" fill="url(#poolPhoto)" role="img" aria-label="Photo of a child smiling in a sparkling resort pool"/>
    </g>
    <circle cx="143" cy="522" r="150" fill="var(--ocean-mid)"/>
    <circle cx="143" cy="522" r="140" fill="url(#spaPhoto)" clip-path="url(#spaClip)" role="img" aria-label="Spa still life with orchid, bamboo, rolled towel and candle"/>
    <path d="M318,212 Q450,120 610,118 Q622,320 612,512 Q450,515 318,432 Z" fill="var(--slate)"/>
  </svg>

  <section class="services">
    <h2 class="services__title">Maintenance</h2>
    <ul class="services__list">
      <li>Regular Maintenance Services</li>
      <li>Weekly Pool/Spa Service</li>
      <li>One Time Clean-Ups</li>
      <li>DE Filter Cleaning</li>
      <li>Drain Pool &amp; Refill</li>
      <li>Impellers</li>
      <li>Valves</li>
      <li>Algae Removal</li>
      <li>Back Wash</li>
      <li>Water Testing &amp; Balancing</li>
      <li>Equipment Inspection</li>
      <li>Skimming, Brushing, &amp; Leafing</li>
    </ul>
    <p class="services__note">Emergency service 24 hours per day, 7 days per week</p>
  </section>
  <div class="services__rule"></div>

  <section class="contact">
    <div class="logo"><span class="logo__mark"></span><span class="logo__name">PBS</span></div>
    <p class="contact__tagline">Sparkling Results</p>
    <svg class="contact__icon" width="62" height="62" viewBox="0 0 62 62" aria-hidden="true">
      <circle cx="31" cy="31" r="28" fill="none" stroke="#fff" stroke-width="3"/>
      <path d="M22 18c2-1 3 0 4 2l2 5c0 2-2 3-2 4 1 3 4 6 7 7 1 0 2-2 4-2l5 2c2 1 3 2 2 4-1 3-4 5-7 4-9-2-16-9-18-18-1-3 1-6 3-8z" fill="#fff"/>
      <path d="M34 18a10 10 0 0 1 10 10M34 23a5 5 0 0 1 5 5" fill="none" stroke="#fff" stroke-width="2" stroke-linecap="round"/>
    </svg>
    <p class="contact__phone">702-555-0187</p>
    <p class="contact__line">rkelvane@basinstewardsgroup.com</p>
    <p class="contact__line">www.premier-basin-stewardsgrp.com</p>
  </section>

  <section class="cover">
    <div class="logo"><span class="logo__mark"></span><span class="logo__name">PBS</span></div>
    <h1 class="cover__headline">Premier Basin<br>Stewards</h1>
    <p class="cover__slogan">Our slogan is "Sparkling Results"</p>
    <p class="cover__web">www.premier-basin-stewardsgrp.com</p>
  </section>
</div>
</body>
</html>
```